Amber Tides: Lantern Tales from Seven Winters by the Northern Sea and Other Small Wonders

Good day! I am excited to work again with you, amazing designers! This time I am looking for the cover design of my book.
Dimensions 6” x 9”
The book name is as my name project. I love simplicity, but yet that is impactful. I love colours, I don't have a specific colour in mind, but I like the mustard colour as the one in the logo of my company. I am open to ideas! I have attached some cover samples that I like so that it gives a better idea of what I have on mind.
I am looking for something that looks professional, yet, not super serious, that it's approachable to people. Something that calls their attention at first glance.
I am working with my editor and my interior designer as well to finalize this part of the book. I will be working with the person that I select for the book design to finalize it.
About the book, here a passage of an unedited version of the introduction for guidance :
My intention is to take you on a journey to help you to understand what is going on in your mind so that you get out from anything that is holding you back in your life. My intention is to guide you to start fully living and experiencing a life that your mind even have yet conceived. To experience a life where you live fearless and without suffering. Living your life where you are the navigator and the creator of how you are experiencing it and you are living in a world of possibilities where there are no limitations.
For it, we will start to understand more about the mind and about the brain. I am not a neuroscientist and neither I consider my self an expert in the workings of the brain, what I know is the result of my fascination about our brain. This curiosity and the part of me that likes to understand how things work took me to read, research and learn about how our brain works and how its intrinsic mechanisms are subconsciously influencing and limiting us. I encourage you to stay on this part, it can be a bit technical, but understanding how it works will empower you not to allow your mind to dictate the way you approach your life and to live on autopilot.
We will continue to describe how you have been programmed throughout your life, putting you inside a box limited by your subconscious beliefs and ideas about the world. In this part, we will also discuss what ego is, how it is subconsciously limiting you and how the ways of when ego manifests itself are limiting you and making you suffer. Now that you know how you have been enclosed in your mind for all your life, we will move to discuss how you can get out of it. You will learn how to master your emotions to eliminate your suffering and not allow them to control the direction of your life and use them as a mechanism to get out from your programed mind. We continue to discuss how to leverage the power of your mind and harness your power of choice. Finally, I invite you to see yourself as a holistic being so that you start truly living and take control over the direction of your life, by nourishing and taking care of all those aspects of you utilizing their wisdom and synergy to achieve higher connection within yourself, your soul and live your life in a higher level of consciousness with peace, flow, love and purpose.

```html
<!DOCTYPE html>
<html lang="en">
<head>
<meta charset="UTF-8">
<title>Amber Tides — Book Cover</title>
<link rel="stylesheet" href="https://fonts.googleapis.com/css2?family=Anton&family=Open+Sans:wght@700&display=swap">
<style>
  :root {
    --cover-deep: #174d8b;
    --cover-glow: #3574a9;
    --mustard: #fbbd13;
    --title-shadow: #0f2238;
  }
  html, body {
    margin: 0;
    padding: 0;
    width: 840px;
    height: 1200px;
    overflow: hidden;
    background: var(--cover-deep);
  }
  .cover {
    position: relative;
    width: 840px;
    height: 1200px;
    overflow: hidden;
    background: radial-gradient(ellipse 480px 520px at 50% 50%, var(--cover-glow) 0%, #2a6399 45%, var(--cover-deep) 100%);
  }
  .cover-title {
    position: absolute;
    left: 0;
    right: 0;
    top: 282px;
    margin: 0;
    text-align: center;
    font-family: "Anton", "Oswald", sans-serif;
    font-weight: 400;
    font-size: 92px;
    line-height: 1;
    letter-spacing: 2px;
    color: var(--mustard);
    text-shadow: 3px 3px 0 var(--title-shadow);
  }
  .clock-illustration {
    position: absolute;
    left: 306px;
    top: 440px;
    width: 220px;
    height: 220px;
    border-radius: 50%;
    background: radial-gradient(circle at 50% 55%, rgba(251,189,19,0.05) 0%, rgba(251,189,19,0.22) 60%, rgba(251,189,19,0.08) 75%, rgba(251,189,19,0) 76%);
  }
  .subtitle-arc {
    position: absolute;
    left: 0;
    top: 0;
    width: 840px;
    height: 1200px;
  }
  .subtitle-text {
    font-family: "Open Sans", sans-serif;
    font-weight: 700;
    font-size: 21px;
    fill: var(--mustard);
  }
</style>
</head>
<body>
  <main class="cover">
    <h1 class="cover-title">AMBER TIDES</h1>

    <div class="clock-illustration" role="img" aria-label="Line drawing of a ringing alarm clock in mustard yellow"></div>

    <svg class="subtitle-arc" viewBox="0 0 840 1200" aria-label="Lantern Tales from Seven Winters by the Northern Sea and Other Small Wonders">
      <defs>
        <path id="subtitle-curve" d="M 20 618 Q 420 946 824 618" fill="none"/>
      </defs>
      <text class="subtitle-text">
        <textPath href="#subtitle-curve" startOffset="50%" text-anchor="middle">Lantern Tales from Seven Winters by the Northern Sea and Other Small Wonders</textPath>
      </text>
    </svg>
  </main>
</body>
</html>
```